One page (Bach and front) flyer graphic composition with all content provided

We need, by Sunday evening at the latest term, to have the enclosed page graphically worked. It will be inserted in a Fair Catalog. Dimensions 20x20We enclose logo and picture to include and draft. Don't consider the Power Point we include only to handle you content: take it from here and decide how to paste it in page to your own judgment.DLW is a software company, producing for investment market. image to give: SERIOUS, COMPETENT, STRAIGHT TO THE POINT and, most important, CREDIBLE company

Target Market(s)

Investors

Font styles to use
Serif

Colors
276eb1
0355a3
ffffff

Requirements
Must have
• Clear, strong Logo in the front page
• The picture on the back
Nice to have
• Credibility, space, clearness
Should not have
• Confusion, too much "loud"

```html
<!DOCTYPE html>
<html lang="en">
<head>
<meta charset="utf-8">
<title>DLW – Fair Catalog Page</title>
<link href="https://fonts.googleapis.com/css2?family=Montserrat:wght@300;400;700&display=swap" rel="stylesheet">
<style>
  :root {
    --blue: #276eb1;
    --blue-deep: #0355a3;
    --blue-bright: #1a4fd0;
    --white: #ffffff;
    --ink: #141414;
    --black: #000000;
    --page-bg: #e9e9e6;
    --rule: #c9c9c9;
  }
  * { margin: 0; padding: 0; box-sizing: border-box; }
  html, body {
    width: 1200px; height: 1200px; overflow: hidden;
    background: var(--page-bg);
    font-family: "Montserrat", Arial, sans-serif;
  }
  .sheet {
    position: relative; width: 1200px; height: 1200px;
  }
  .card {
    position: absolute; left: 325px; width: 550px; height: 550px;
    background: var(--white); overflow: hidden;
    box-shadow: 0 6px 18px rgba(0,0,0,.18);
  }
  .card--front { top: 33px; }
  .card--back { top: 617px; }

  /* front */
  .front-disc {
    position: absolute; left: -113px; top: -44px;
    width: 480px; height: 480px; border-radius: 50%;
    background: linear-gradient(160deg, var(--blue-bright) 0%, var(--blue) 45%, var(--blue-deep) 100%);
  }
  .brand {
    position: absolute; display: flex; align-items: center; gap: 6px;
    color: var(--blue-bright); font-weight: 700; letter-spacing: .5px;
  }
  .brand__dot { border-radius: 50%; background: var(--blue-bright); }
  .brand--front { right: 34px; top: 38px; font-size: 38px; }
  .brand--front .brand__dot { width: 38px; height: 38px; }
  .tagline {
    position: absolute; right: 34px; top: 465px;
    font-size: 37px; font-weight: 400; color: var(--ink);
  }
  .tagline strong { color: var(--blue-bright); font-weight: 700; }
  .url {
    font-size: 11px; letter-spacing: 5px; color: var(--ink);
  }
  .url--front { position: absolute; right: 32px; top: 516px; }

  /* back */
  .back-band {
    position: absolute; left: 0; top: 0; width: 550px; height: 314px;
    background: var(--black);
  }
  .headline {
    position: absolute; left: 36px; top: 118px; color: var(--white);
    font-weight: 300; line-height: 1;
  }
  .headline__small { display: block; font-size: 29px; letter-spacing: 1px; }
  .headline__large { display: block; font-size: 52px; margin-top: 8px; }
  .photo {
    position: absolute; left: 318px; top: 36px; width: 205px; height: 260px;
    background: radial-gradient(ellipse at 55% 35%, #6b6450 0%, #2a2822 45%, #000 80%);
  }
  .invite {
    position: absolute; left: 36px; top: 360px;
    color: var(--blue); font-size: 17px; line-height: 1.3; letter-spacing: .4px;
  }
  .venue {
    position: absolute; left: 35px; top: 410px;
    color: var(--ink); font-size: 23px; letter-spacing: .3px;
  }
  .venue strong { color: var(--blue-deep); font-weight: 700; }
  .back-footer {
    position: absolute; left: 36px; right: 34px; bottom: 30px;
    display: flex; align-items: flex-end; justify-content: space-between;
  }
  .back-footer .url {
    flex: 1; margin-right: 10px; padding-bottom: 2px;
    border-bottom: 1px solid var(--rule);
  }
  .brand--back { position: static; font-size: 30px; }
  .brand--back .brand__dot { width: 30px; height: 30px; }
</style>
</head>
<body>
<main class="sheet">
  <section class="card card--front" aria-label="Front page">
    <div class="front-disc"></div>
    <div class="brand brand--front"><span class="brand__dot"></span><span>DLW</span></div>
    <p class="tagline">Your Money <strong>Growth</strong></p>
    <p class="url url--front">www.dlwinvest.io</p>
  </section>

  <section class="card card--back" aria-label="Back page">
    <div class="back-band"></div>
    <h1 class="headline">
      <span class="headline__small">WE ARE WAITING</span>
      <span class="headline__large">FOR YOU!</span>
    </h1>
    <div class="photo" role="img" aria-label="Photo of a martini glass filled with gold coins and ice cubes on a black background"></div>
    <p class="invite">Ask your invitation to our DLW Hostess<br>and be welcommed to:</p>
    <p class="venue">Presidential Suite <strong>Level 18</strong></p>
    <div class="back-footer">
      <p class="url">www.dlwinvest.io</p>
      <div class="brand brand--back"><span class="brand__dot"></span><span>DLW</span></div>
    </div>
  </section>
</main>
</body>
</html>
```